Lien Post Card - (5.5 x 8.5)

FRONT OF POSTCARD
Is a Property Lien Putting Your Home at Risk?
HOA Liens • Tax Liens • Municipal Charges • Other Property-Related Liens
You may have options to resolve outstanding liens and protect your home.
A Refinance or Home Equity Line of Credit (HELOC) may help you:
✔ Pay off qualifying liens
✔ Consolidate debt into one manageable payment
✔ Access your home's equity
✔ Improve your financial flexibility
✔ Avoid additional penalties, fees, or collection actions
Don't wait until the situation becomes more difficult.
Call today for a confidential review of your options.
Bluecove Lending Group, Inc.
(800) 641-2907 x 42
www.bluecovelending.com
NMLS #738150
BACK OF POSTCARD
Your Home Equity Could Be the Solution
If you have received notices regarding:
• Delinquent Property Taxes
• HOA or Condo Association Assessments
• Municipal Utility Liens
• Special Assessments
• Other Property-Related Obligations
You may qualify for financing options designed to help satisfy those obligations and bring your property current.
Our experienced mortgage professionals can review your situation and discuss available programs, including:
• Cash-Out Refinancing
• Home Equity Lines of Credit (HELOCs)
• Home Equity Loans
• Debt Consolidation Solutions
Free Consultation • No Obligation
Contact Marcus Whitfield today at (800) 641-2907 x42 or mwhitfield@bluecovelending.com (NMLS #84617)

```html
<!DOCTYPE html>
<html lang="en">
<head>
<meta charset="utf-8">
<title>Bluecove Lending Group – Lien Postcard</title>
<link rel="stylesheet" href="https://fonts.googleapis.com/css2?family=Poppins:wght@400;500;600;700&family=Libre+Baskerville:wght@700&display=swap">
<style>
:root{
  --sheet:#dcdcdc;
  --paper:#ffffff;
  --navy:#1a4f9c;
  --navy-deep:#1b4a93;
  --blue-light:#6a9ad6;
  --gold:#b5861e;
  --gold-soft:#f9c36f;
  --ink:#222222;
  --label:#8a8a8a;
  --check:#5b8fd6;
}
*{margin:0;padding:0;box-sizing:border-box}
html,body{width:953px;height:1200px;overflow:hidden;background:var(--sheet)}
body{position:relative;font-family:"Poppins",sans-serif;color:var(--ink)}
.side-label{position:absolute;left:90px;font-family:"Libre Baskerville",serif;font-weight:700;font-size:27px;color:var(--label);letter-spacing:1px}
.side-label.front{top:48px}
.side-label.back{top:1124px}
.card{position:absolute;background:var(--paper);overflow:hidden;box-shadow:4px 6px 10px rgba(0,0,0,.22)}
.card-front{left:92px;top:89px;width:758px;height:490px}
.card-back{left:91px;top:622px;width:757px;height:491px}
.abs{position:absolute}

/* brand */
.brand{display:flex;align-items:center;gap:8px;font-weight:700;color:var(--navy)}
.brand .mark{width:22px;height:22px;border-radius:50%;background:var(--gold-soft);flex:none}
.brand-front{left:40px;top:68px;font-size:17px}
.brand-back{left:436px;top:432px;width:170px;font-size:11px;line-height:14px;justify-content:center;text-align:center}
.brand-back .mark{width:14px;height:14px}
.nmls-small{left:446px;top:470px;width:130px;text-align:center;font-size:7.5px;color:#333}

/* front */
.headline{left:40px;top:150px;font-weight:700;font-size:29.5px;line-height:31px;color:var(--navy)}
.headline .accent{color:var(--gold)}
.lien-types{left:40px;top:254px;font-size:12.5px;line-height:15.5px}
.heloc-intro{left:40px;top:298px;font-size:12.5px;line-height:15.5px;font-weight:500;color:var(--navy)}
.benefits{left:40px;top:335px;list-style:none;font-size:12.8px;line-height:15.4px}
.benefits li{position:relative;padding-left:15px}
.benefits li svg{position:absolute;left:0;top:5px}
.call-band{left:0;top:426px;width:395px;height:24px;background:var(--gold);clip-path:polygon(0 0,380px 0,395px 24px,0 24px);color:#fff;font-weight:600;font-size:12.3px;line-height:24px;padding-left:40px}
.dont-wait{left:405px;top:424px;font-weight:600;font-size:12.3px;color:var(--navy)}
.contact-bar{left:0;top:450px;width:758px;height:40px;background:linear-gradient(90deg,var(--navy-deep),var(--blue-light));color:#fff;display:flex;align-items:center}
.contact-bar .phone{position:absolute;left:40px;display:flex;align-items:center;gap:9px;font-weight:600;font-size:19.5px}
.contact-bar .web{position:absolute;left:273px;display:flex;align-items:center;gap:10px;font-weight:600;font-size:19.5px}
.contact-bar .nmls{position:absolute;right:28px;font-size:14px}
.badge{left:386px;top:163px;width:134px;height:134px;border-radius:50%;background:linear-gradient(160deg,#2d63b0,var(--navy-deep));border:3px solid var(--gold-soft);color:#fff;font-weight:600;font-size:12px;line-height:15.5px;display:flex;align-items:center;justify-content:center;text-align:center;padding:0 8px}

/* back */
.back-title{left:46px;top:30px;font-weight:700;font-size:29.5px;line-height:30px;color:var(--navy)}
.back-lead{left:45px;top:110px;font-size:12.5px}
.notice-list{left:45px;top:140px;list-style:none;font-size:12.5px;line-height:15.4px}
.notice-list li::before,.program-list li::before{content:"• ";color:var(--check)}
.qualify{left:45px;top:231px;width:350px;font-size:12.5px;line-height:15.4px}
.panel{left:413px;top:0;width:344px;height:382px;background:linear-gradient(120deg,#214f9c,#3f74c0 55%,#6a9ad6);border-bottom-left-radius:48px;color:#fff}
.panel-intro{left:34px;top:38px;width:290px;font-size:12.5px;line-height:15.4px}
.program-list{left:34px;top:100px;list-style:none;font-size:12.5px;line-height:15.6px}
.program-list li::before{color:#fff}
.pill{top:190px;height:28px;background:var(--gold-soft);color:var(--navy);font-weight:700;font-size:13.3px;display:flex;align-items:center;justify-content:center;gap:5px}
.pill-consult{left:26px;width:157px}
.pill-obligation{left:190px;width:127px}
.contact-title{left:34px;top:254px;font-weight:600;font-size:20px}
.rep-name{left:34px;top:292px;font-weight:600;font-size:12.5px;color:var(--gold-soft)}
.rep-line{left:34px;display:flex;align-items:center;gap:6px;font-size:12px;white-space:nowrap}
.rep-phone{top:312px}
.rep-email{top:332px;font-size:11px}
.portrait{left:668px;top:230px;width:89px;height:261px;background:linear-gradient(180deg,#2b2b2b,#4a3a32 45%,#1c1c1c);border-top-left-radius:44px}
</style>
</head>
<body>

<div class="side-label front">FRONT</div>

<section class="card card-front">
  <svg class="abs" style="left:0;top:0" width="758" height="490" viewBox="0 0 758 490">
    <defs>
      <clipPath id="front-photo-clip"><circle cx="650" cy="125" r="255"/></clipPath>
      <linearGradient id="front-photo-tone" x1="0" y1="0" x2="1" y2="1">
        <stop offset="0" stop-color="#d9d6d2"/><stop offset=".5" stop-color="#8a8f99"/><stop offset="1" stop-color="#c9c2b8"/>
      </linearGradient>
    </defs>
    <circle cx="650" cy="125" r="268" fill="none" stroke="var(--navy)" stroke-width="3"/>
    <circle cx="650" cy="125" r="261" fill="none" stroke="var(--gold-soft)" stroke-width="5"/>
    <rect x="390" y="0" width="368" height="400" fill="url(#front-photo-tone)" clip-path="url(#front-photo-clip)" role="img" aria-label="Photo of a worried couple reviewing bills at home"/>
  </svg>

  <div class="abs brand brand-front"><span class="mark"></span>Bluecove Lending Group, Inc.</div>

  <h1 class="abs headline">IS A PROPERTY LOAN<br>PUTTING <span class="accent">YOUR HOME</span><br>AT RISK?</h1>

  <p class="abs lien-types">• HOA Liens &nbsp;• Tax Liens &nbsp;• Municipal Charges<br>• Other Property-Related Liens</p>

  <p class="abs heloc-intro">A Refinance or Home Equity Line of Credit (HELOC)<br>may help you:</p>

  <ul class="abs benefits">
    <li><svg width="10" height="8" viewBox="0 0 10 8"><path d="M1 4l3 3 5-6" fill="none" stroke="var(--check)" stroke-width="1.8"/></svg>Pay off qualifying liens</li>
    <li><svg width="10" height="8" viewBox="0 0 10 8"><path d="M1 4l3 3 5-6" fill="none" stroke="var(--check)" stroke-width="1.8"/></svg>Consolidate debt into one manageable payment</li>
    <li><svg width="10" height="8" viewBox="0 0 10 8"><path d="M1 4l3 3 5-6" fill="none" stroke="var(--check)" stroke-width="1.8"/></svg>Access your home's equity</li>
    <li><svg width="10" height="8" viewBox="0 0 10 8"><path d="M1 4l3 3 5-6" fill="none" stroke="var(--check)" stroke-width="1.8"/></svg>Improve your financial flexibility</li>
    <li><svg width="10" height="8" viewBox="0 0 10 8"><path d="M1 4l3 3 5-6" fill="none" stroke="var(--check)" stroke-width="1.8"/></svg>Avoid additional penalties, fees, or collection actions</li>
  </ul>

  <div class="abs badge">You may have options to resolve outstanding liens and protect your home.</div>

  <div class="abs call-band">Call today for a confidential review of your options.</div>
  <p class="abs dont-wait">Don't wait until the situation becomes more difficult.</p>

  <div class="abs contact-bar">
    <span class="phone"><svg width="13" height="13" viewBox="0 0 24 24"><path d="M6.6 10.8a15 15 0 006.6 6.6l2.2-2.2a1 1 0 011-.25 11 11 0 003.6.6 1 1 0 011 1V20a1 1 0 01-1 1A17 17 0 013 4a1 1 0 011-1h3.5a1 1 0 011 1 11 11 0 00.6 3.6 1 1 0 01-.25 1z" fill="var(--gold-soft)"/></svg>(800) 641-2907 x 42</span>
    <span class="web"><svg width="13" height="13" viewBox="0 0 24 24" fill="none" stroke="var(--gold-soft)" stroke-width="2.4"><circle cx="12" cy="12" r="10"/><path d="M2 12h20M12 2a15 15 0 010 20M12 2a15 15 0 000 20"/></svg>www.bluecovelending.com</span>
    <span class="nmls">NMLS #738150</span>
  </div>
</section>

<section class="card card-back">
  <svg class="abs" style="left:0;top:0" width="757" height="491" viewBox="0 0 757 491">
    <defs>
      <clipPath id="back-photo-clip"><circle cx="176" cy="560" r="264"/></clipPath>
      <linearGradient id="back-photo-tone" x1="0" y1="0" x2="1" y2="1">
        <stop offset="0" stop-color="#e6e6e6"/><stop offset=".5" stop-color="#6e6e6e"/><stop offset="1" stop-color="#3a3a3a"/>
      </linearGradient>
    </defs>
    <circle cx="176" cy="560" r="280" fill="none" stroke="var(--navy)" stroke-width="3"/>
    <circle cx="176" cy="560" r="271" fill="none" stroke="var(--gold-soft)" stroke-width="5"/>
    <rect x="0" y="280" width="460" height="211" fill="url(#back-photo-tone)" clip-path="url(#back-photo-clip)" role="img" aria-label="Black and white photo of a large brick house in winter"/>
  </svg>

  <h2 class="abs back-title">Your Home Equity<br>Could Be the Solution</h2>
  <p class="abs back-lead">If you have received notices regarding:</p>
  <ul class="abs notice-list">
    <li>Delinquent Property Taxes</li>
    <li>HOA or Condo Association Assessments</li>
    <li>Municipal Utility Liens</li>
    <li>Special Assessments</li>
    <li>Other Property-Related Obligations</li>
  </ul>
  <p class="abs qualify">You may qualify for financing options designed to help satisfy those obligations and bring your property current.</p>

  <div class="abs panel">
    <p class="abs panel-intro">Our experienced mortgage professionals can review your situation and discuss available programs, including:</p>
    <ul class="abs program-list">
      <li>Cash-Out Refinancing</li>
      <li>Home Equity Lines of Credit (HELOCs)</li>
      <li>Home Equity Loans</li>
      <li>Debt Consolidation Solutions</li>
    </ul>
    <div class="abs pill pill-consult"><svg width="14" height="14" viewBox="0 0 24 24" fill="none" stroke="var(--navy)" stroke-width="2.6"><path d="M4 15v-3a8 8 0 0116 0v3"/><rect x="3" y="14" width="4" height="6" rx="1" fill="var(--navy)"/><rect x="17" y="14" width="4" height="6" rx="1" fill="var(--navy)"/></svg>Free Consultation</div>
    <div class="abs pill pill-obligation"><svg width="13" height="13" viewBox="0 0 24 24" fill="none" stroke="var(--navy)" stroke-width="2.6"><circle cx="12" cy="12" r="9"/><path d="M6 6l12 12"/></svg>No Obligation</div>
    <h3 class="abs contact-title">Contact</h3>
    <p class="abs rep-name">Marcus Whitfield</p>
    <p class="abs rep-line rep-phone"><svg width="11" height="11" viewBox="0 0 24 24"><path d="M6.6 10.8a15 15 0 006.6 6.6l2.2-2.2a1 1 0 011-.25 11 11 0 003.6.6 1 1 0 011 1V20a1 1 0 01-1 1A17 17 0 013 4a1 1 0 011-1h3.5a1 1 0 011 1 11 11 0 00.6 3.6 1 1 0 01-.25 1z" fill="var(--gold-soft)"/></svg>(800) 641-2907 x42</p>
    <p class="abs rep-line rep-email"><svg width="12" height="10" viewBox="0 0 24 18" fill="none" stroke="var(--gold-soft)" stroke-width="2.4"><rect x="1" y="1" width="22" height="16" rx="1"/><path d="M1 2l11 8 11-8"/></svg>mwhitfield@bluecovelending.com</p>
  </div>

  <div class="abs portrait" role="img" aria-label="Portrait of the loan officer in a hat and dark jacket"></div>

  <div class="abs brand brand-back"><span class="mark"></span>Bluecove Lending Group, Inc.</div>
  <p class="abs nmls-small">(NMLS #84617)</p>
</section>

<div class="side-label back">BACK</div>

</body>
</html>
```